Mortgage Loan officer needs clean/modern business card design

Looking for a clean, modern 2-sided business card design. We like the earth tones used in our logo and website http://varnhill-lending.com . Would also like to incorporate: 1) Something special to make our card stand out - a pop of color or embossed logo, for instance and 2) please include "Mortgage Loans" "Reverse Mortgages" "Private Money Loans" on back of card with the logo.

Front: Needs to include agent/company license info - see website. Agent name: Marco Lindqvist

Here are fonts and colors used for our logo:
Font: Avenir Next
Colors:
#2c3539 - Dark Gray
#576870 - Light Gray
#ffffff - Background White

Target Market(s)

Prospects and current clients. Will also be distributing to people in professional network (attorneys and CPAs)

Industry/Entity Type

Business

Contact Information for Business Card

Include agent name, contact info, website on front, licensing info for agent an company. Logo and services offered on back

Font styles to use
Other font styles liked:
• Avenir Next

Requirements
Must have
• See project description
Should not have
• Nothing cheesy

```html
<!DOCTYPE html>
<html lang="en">
<head>
<meta charset="utf-8">
<title>Varnhill Lending – Business Card</title>
<link rel="stylesheet" href="https://fonts.googleapis.com/css2?family=Open+Sans:wght@400;600;700&family=Nunito+Sans:wght@300&display=swap">
<style>
  :root {
    --backdrop: #e9e6e3;
    --card-white: #f4f4f4;
    --card-black: #111111;
    --ink-dark: #2c3539;
    --ink-mid: #576870;
    --rule: #8a969b;
    --ring: #9b9694;
    --logo-taupe: #b9b1ac;
    --service-white: #f2f2f2;
  }
  * { margin: 0; padding: 0; box-sizing: border-box; }
  html, body { width: 1200px; height: 900px; overflow: hidden; }
  body {
    background: var(--backdrop);
    font-family: "Open Sans", sans-serif;
    position: relative;
  }
  .card {
    position: absolute;
    width: 558px;
    height: 343px;
    border-radius: 26px;
    box-shadow: 0 6px 18px rgba(0,0,0,0.15);
  }
  .card-front {
    left: 330px; top: 62px;
    background: var(--card-white);
    color: var(--ink-mid);
    text-align: center;
    padding-top: 54px;
  }
  .agent-name {
    font-size: 26px; font-weight: 600; color: var(--ink-mid);
    letter-spacing: 0.5px; line-height: 1.1;
  }
  .agent-title {
    font-size: 14px; font-weight: 600; color: var(--ink-dark);
    margin-top: 6px;
  }
  .title-rule {
    width: 122px; height: 1px; background: var(--rule);
    margin: 6px auto 10px;
  }
  .contact-list, .office-address {
    font-size: 15px; line-height: 21px; color: var(--ink-mid);
  }
  .office-address { margin-top: 10px; }
  .office-name { font-weight: 700; color: var(--ink-dark); }
  .card-back {
    left: 400px; top: 505px;
    background: var(--card-black);
  }
  .logo-ring {
    position: absolute; left: 174px; top: 48px;
    width: 206px; height: 206px; border-radius: 50%;
    border: 1.5px solid var(--ring);
    display: flex; align-items: center; justify-content: center;
    text-align: center;
  }
  .logo-name {
    font-family: "Nunito Sans", sans-serif; font-weight: 300;
    font-size: 21px; line-height: 1.25; color: var(--logo-taupe);
  }
  .service-list {
    position: absolute; left: 0; right: 0; top: 285px;
    display: flex; justify-content: center; gap: 10px;
    list-style: none;
    font-size: 15px; font-weight: 600; color: var(--service-white);
  }
  .service-list li::before {
    content: ""; display: inline-block; width: 5px; height: 5px;
    border-radius: 50%; background: var(--service-white);
    margin-right: 6px; vertical-align: middle;
  }
</style>
</head>
<body>
  <section class="card card-front">
    <h1 class="agent-name">MARCO LINDQVIST</h1>
    <p class="agent-title">DIRECTOR</p>
    <div class="title-rule"></div>
    <p class="contact-list">
      (514)555-0142<br>
      (514)555-018377<br>
      info@varnhill.com<br>
      www.varnhill-lending.com
    </p>
    <p class="office-address">
      <span class="office-name">Varnhill Lending</span><br>
      Example street Ave 63<br>
      12345 country.
    </p>
  </section>

  <section class="card card-back">
    <div class="logo-ring">
      <p class="logo-name">The Varnhill<br>Group</p>
    </div>
    <ul class="service-list">
      <li>Mortgage Loans</li>
      <li>Reverse Mortgages</li>
      <li>Private Money Loans</li>
    </ul>
  </section>
</body>
</html>
```